Gil’s NY Pizza Menu & Logo design

Looking for something that I can put on an 8.5x14 and also larger for an in-house menu to laminate. This is for a pizzeria, it doesn’t need to have that logo on it, I need a new design that is clean and I can use for shirts and signs. Want something modern and clean. This pizzeria is established and we are looking to rebrand. I have the current logo on the menu submission.

Target Market(s)

Looking for a new logo and menu design for my Pizzeria.

Industry/Entity Type

restaurant

Font styles to use
Sans Serif

Requirements
Must have
• Clean and fresh design for the logo that works for the menu, shirts, and signs.
Nice to have
• Open to any design, I want something completely catchy and updated.

```html
<!DOCTYPE html>
<html lang="en">
<head>
<meta charset="utf-8">
<title>Gil’s NY Pizza — Menu</title>
<link href="https://fonts.googleapis.com/css2?family=Montserrat:wght@500;600&family=Rubik:wght@600;700;800&display=swap" rel="stylesheet">
<style>
:root{
  --ink:#000;
  --paper:#fff;
  --stage:#e8e5df;
  --red:#e21f26;
  --green:#3f9a36;
  --cream:#fbeed2;
  --text:#fff;
  --dark-text:#111;
  --skyline-dark:#2a2a2a;
  --skyline-light:#e4e4e4;
}
*{margin:0;padding:0;box-sizing:border-box}
html,body{width:1200px;height:800px;overflow:hidden;background:var(--stage)}
body{font-family:"Montserrat",sans-serif;position:relative}
.menu{position:absolute;left:20px;top:47px;width:1160px;height:705px;box-shadow:0 4px 14px rgba(0,0,0,.25)}
.panel{position:absolute;top:0;height:705px;overflow:hidden}
.panel--left{left:0;width:429px;background:var(--ink)}
.panel--center{left:429px;width:301px;background:var(--paper)}
.panel--right{left:730px;width:430px;background:var(--ink)}
.frame{position:absolute;left:0;width:100%;height:22px}
.skyline{position:absolute;z-index:0}
.panel--left .skyline,.panel--right .skyline{background:linear-gradient(180deg,rgba(42,42,42,0) 0%,var(--skyline-dark) 45%,#333 100%)}
.panel--center .skyline{background:linear-gradient(180deg,rgba(255,255,255,0) 0%,var(--skyline-light) 40%,#dcdcdc 100%)}
.section-title{position:absolute;left:0;width:100%;display:flex;justify-content:center;align-items:center;gap:4px;
  font-family:"Rubik",sans-serif;font-weight:700;font-size:20px;line-height:22px;letter-spacing:.2px;z-index:2}
.section-title .chev{width:9px;height:22px;background:currentColor;clip-path:polygon(0 0,35% 0,100% 50%,35% 100%,0 100%,65% 50%)}
.section-title .chev--end{transform:scaleX(-1)}
.section-title--red{color:var(--red)}
.section-title--green{color:var(--green)}
.section-title--dark{color:var(--dark-text)}
.box{position:absolute;border:1.2px solid;border-top:none;padding:5px 4px 4px 8px;z-index:2}
.box--red{border-color:var(--red)}
.box--green{border-color:var(--green)}
.box--dark{border-color:var(--dark-text)}
.item-head{display:flex;justify-content:space-between;font-family:"Rubik",sans-serif;font-weight:600;font-size:9.4px;line-height:13.3px}
.item-head .price{color:var(--text);font-weight:700}
.item-desc{font-size:8.9px;line-height:13.3px;color:var(--text);font-weight:500}
.box--red .item-head .name{color:var(--red)}
.box--green .item-head .name{color:var(--green)}
.box--dark .item-head,.box--dark .item-desc,.box--dark .item-head .price{color:var(--dark-text)}
.toppings{position:absolute;left:37px;top:612px;width:330px;font-size:8.9px;line-height:13.3px;color:var(--text);z-index:2}
.toppings .label-red{color:var(--red);font-family:"Rubik",sans-serif;font-weight:600}
.toppings .label-green{color:var(--green);font-family:"Rubik",sans-serif;font-weight:600}
.brand{position:absolute;left:0;top:60px;width:100%;text-align:center;font-family:"Rubik",sans-serif;font-weight:800;
  font-size:46px;line-height:50px;color:var(--red);z-index:2}
.favorite{position:absolute;left:0;top:280px;width:100%;text-align:center;font-family:"Rubik",sans-serif;font-weight:800;
  font-size:15px;line-height:20px;color:var(--dark-text);z-index:2}
.favorite .bullets{margin-top:5px}
.salad-row{display:flex;justify-content:space-between}
.salad-row .item-desc{width:240px}
.sizes{display:flex;font-size:9px;line-height:13.3px;color:var(--text);white-space:nowrap}
.sizes span{padding:0 3px;border-left:1px solid var(--text)}
.sizes span:first-child{border-left:none}
.sizes b{font-family:"Rubik",sans-serif;font-weight:700;margin-left:2px}
.dressings{position:absolute;left:36px;top:519px;font-size:8.9px;line-height:13.3px;color:var(--text);z-index:2}
.dressings .label-red{color:var(--red);font-family:"Rubik",sans-serif;font-weight:600}
</style>
</head>
<body>
<main class="menu">

  <!-- Left panel -->
  <section class="panel panel--left">
    <svg class="frame" style="top:15px" viewBox="0 0 429 22" aria-hidden="true"><path d="M22 6 H407 M22 6 q-9 0 -9 7 q0 5 5 5 M407 6 q9 0 9 7 q0 5 -5 5" fill="none" stroke="var(--red)" stroke-width="1.6"/></svg>
    <svg class="frame" style="top:673px" viewBox="0 0 429 22" aria-hidden="true"><path d="M22 16 H407 M22 16 q-9 0 -9 -7 q0 -5 5 -5 M407 16 q9 0 9 -7 q0 -5 -5 -5" fill="none" stroke="var(--green)" stroke-width="1.6"/></svg>
    <div class="skyline" style="left:0;top:520px;width:429px;height:185px" role="img" aria-label="Faint city skyline illustration"></div>

    <h2 class="section-title section-title--red" style="top:36px"><span class="chev"></span>LUNCH SPECIALS<span class="chev chev--end"></span></h2>
    <div class="box box--red" style="left:29px;top:63px;width:371px;height:114px">
      <div class="item-head"><span class="name">2 Slices of Pizza &amp; 20 oz Drink</span><span class="price">$8.99</span></div>
      <p class="item-desc">Choose your drink. Add a slice topping if you'd like.</p>
      <div class="item-head"><span class="name">Slice of Pizza &amp; Small Salad &amp; 20 oz Drink</span><span class="price">$9.99</span></div>
      <p class="item-desc">Choice of dressing and drink.</p>
      <div class="item-head"><span class="name">Slice of Pizza &amp; 6 Wings &amp; 20 oz Drink</span><span class="price">$12.99</span></div>
      <p class="item-desc">Choose wing sauce and your drink.</p>
      <div class="item-head"><span class="name">Any Philly Cheesesteak &amp; 20 oz Drink</span><span class="price">$10.99</span></div>
      <p class="item-desc">Choose your drink. Philly add-ons available.</p>
    </div>

    <h2 class="section-title section-title--green" style="top:196px"><span class="chev"></span>DAILY SPECIALS<span class="chev chev--end"></span></h2>
    <div class="box box--green" style="left:29px;top:223px;width:371px;height:114px">
      <div class="item-head"><span class="name">Medium Cheese Pizza &amp; 10 Wings</span><span class="price">$29.95</span></div>
      <p class="item-desc">Choose wing style and sauce.</p>
      <div class="item-head"><span class="name">Large 16" Cheese Pizza &amp; 20 Wings</span><span class="price">$39.95</span></div>
      <p class="item-desc">Choose wing style and sauce, then add pizza toppings if you'd like.</p>
      <div class="item-head"><span class="name">Large 16" Pizzas</span><span class="price">$30.99</span></div>
      <p class="item-desc">Add toppings to either pie.</p>
      <div class="item-head"><span class="name">18" Cheese Pizza, 24 Wings &amp; 2 Liter Soda</span><span class="price">$45.99</span></div>
      <p class="item-desc">Choose wing style, sauce, soda, and pizza toppings.</p>
    </div>

    <h2 class="section-title section-title--red" style="top:356px"><span class="chev"></span>CALZONES<span class="chev chev--end"></span></h2>
    <div class="box box--red" style="left:29px;top:384px;width:371px;height:142px">
      <div class="item-head"><span class="name">Traditional Calzone</span><span class="price">$11.99</span></div>
      <p class="item-desc">Mozzarella &amp; Ricotta Cheese.</p>
      <div class="item-head"><span class="name">NY Supreme Calzone</span><span class="price">$14.99</span></div>
      <p class="item-desc">Pepperoni, Sausage, Mushrooms, Onions, Green Peppers,<br>Mozzarella, &amp; Ricotta Cheese.</p>
      <div class="item-head"><span class="name">Veggie Calzone</span><span class="price">$12.99</span></div>
      <p class="item-desc">Black Olives, Mushrooms, Onions, Green Peppers, Mozzarella,<br>&amp; Ricotta Cheese.</p>
      <div class="item-head"><span class="name">Meat Lovers Calzone</span><span class="price">$14.99</span></div>
      <p class="item-desc">Sausage, Pepperoni, Ham, Bacon, Mozzarella, &amp; Ricotta Cheese.</p>
    </div>

    <div class="toppings" style="top:542px">
      <p class="label-red">Extra calzone toppings:</p>
      <p class="label-green">$.75 each:</p>
      <p>Anchovies | Banana Peppers | Black Olives | Green Olives<br>Extra Cheese | Extra Sauce | Garlic | Green Peppers | Ham |<br>Jalapeños | Meatballs | Mushrooms | Onions | Pepperoni |<br>Pineapple | Salami | Sausage | Spinach | Tomatoes | Bacon |<br>Broccoli.</p>
      <p class="label-green">$1.00 each:</p>
      <p>Artichokes | Bacon | Chicken | Eggplant | Green Olives | Meatball |<br>Ricotta</p>
    </div>
  </section>

  <!-- Center panel -->
  <section class="panel panel--center">
    <svg class="frame" style="top:15px" viewBox="0 0 301 22" aria-hidden="true"><path d="M28 6 H273 M28 6 q-9 0 -9 7 q0 5 5 5 M273 6 q9 0 9 7 q0 5 -5 5" fill="none" stroke="var(--dark-text)" stroke-width="1.6"/></svg>
    <svg class="frame" style="top:673px" viewBox="0 0 301 22" aria-hidden="true"><path d="M28 16 H273 M28 16 q-9 0 -9 -7 q0 -5 5 -5 M273 16 q9 0 9 -7 q0 -5 -5 -5" fill="none" stroke="var(--dark-text)" stroke-width="1.6"/></svg>
    <div class="skyline" style="left:0;top:260px;width:301px;height:445px" role="img" aria-label="Faint illustration of a harbor statue and city towers"></div>

    <h1 class="brand">Gil’s<br>NY Pizza</h1>

    <h2 class="section-title section-title--dark" style="top:246px"><span class="chev"></span>OWNER'S FAVORITE<span class="chev chev--end"></span></h2>
    <div class="favorite">
      <p>THE GIL'S CHICKEN &amp; JALAPEÑO<br>BUILT FOR GIL HIMSELF.</p>
      <p class="bullets">· STONE COOKED PIZZA WINGS<br>· CHEESESTEAKS · CALZONES</p>
    </div>

    <h2 class="section-title section-title--dark" style="top:446px"><span class="chev"></span>DRINKS<span class="chev chev--end"></span></h2>
    <div class="box box--dark" style="left:12px;top:475px;width:278px;height:65px">
      <div class="item-head"><span class="name">20 oz Soda</span><span class="price">$1.99</span></div>
      <p class="item-desc">Doc Fizz, Peak Cola, Sparkle, Orange Soda, Diet Peak Cola.</p>
      <div class="item-head"><span class="name">2 Liter Soda</span><span class="price">$2.99</span></div>
      <p class="item-desc">Doc Fizz, Peak Cola, Sparkle, Orange Soda, Diet Peak Cola.</p>
    </div>

    <h2 class="section-title section-title--dark" style="top:559px"><span class="chev"></span>DESSERTS<span class="chev chev--end"></span></h2>
    <div class="box box--dark" style="left:12px;top:587px;width:278px;height:63px;padding-top:7px">
      <div class="item-head" style="line-height:17.7px"><span class="name">Cheesecake.</span><span class="price">$4.99</span></div>
      <div class="item-head" style="line-height:17.7px"><span class="name">Tiramisu.</span><span class="price">$5.50</span></div>
      <div class="item-head" style="line-height:17.7px"><span class="name">Cannoli.</span><span class="price">$4.99</span></div>
    </div>
  </section>

  <!-- Right panel -->
  <section class="panel panel--right">
    <svg class="frame" style="top:15px" viewBox="0 0 430 22" aria-hidden="true"><path d="M22 6 H408 M22 6 q-9 0 -9 7 q0 5 5 5 M408 6 q9 0 9 7 q0 5 -5 5" fill="none" stroke="var(--green)" stroke-width="1.6"/></svg>
    <svg class="frame" style="top:673px" viewBox="0 0 430 22" aria-hidden="true"><path d="M22 16 H408 M22 16 q-9 0 -9 -7 q0 -5 5 -5 M408 16 q9 0 9 -7 q0 -5 -5 -5" fill="none" stroke="var(--red)" stroke-width="1.6"/></svg>
    <div class="skyline" style="left:0;top:520px;width:430px;height:185px" role="img" aria-label="Faint illustration of a suspension bridge and skyline"></div>

    <h2 class="section-title section-title--green" style="top:36px"><span class="chev"></span>PIZZA ROLLS<span class="chev chev--end"></span></h2>
    <div class="box box--green" style="left:29px;top:63px;width:373px;height:181px">
      <div class="item-head"><span class="name">Cheese Pizza Roll.</span><span class="price">$11.49</span></div>
      <div class="item-head"><span class="name">Pepperoni Pizza Roll</span><span class="price">$12.99</span></div>
      <p class="item-desc">Pepperoni &amp; Cheese.</p>
      <div class="item-head"><span class="name">Meat Lovers Pizza Roll</span><span class="price">$13.99</span></div>
      <p class="item-desc">Pepperoni, Sausage, Ham, Bacon, &amp; Cheese.</p>
      <div class="item-head"><span class="name">Veggie Pizza Roll</span><span class="price">$13.99</span></div>
      <p class="item-desc">Mushrooms, Green Peppers, Onions, Black Olives, &amp; Cheese.</p>
      <div class="item-head"><span class="name">Supreme Pizza Roll</span><span class="price">$13.99</span></div>
      <p class="item-desc">Pepperoni, Sausage, Mushroom, Green Peppers, Onions, &amp; Cheese.</p>
      <div class="item-head"><span class="name">Buffalo Chicken Pizza Roll</span><span class="price">$13.99</span></div>
      <p class="item-desc">Buffalo Chicken &amp; Cheese.</p>
      <div class="item-head"><span class="name">Chicken, Bacon, Jalapeños &amp; Ranch Pizza Roll</span><span class="price">$13.99</span></div>
      <p class="item-desc">It is what it says, Plus Cheese.</p>
    </div>

    <h2 class="section-title section-title--red" style="top:263px"><span class="chev"></span>SALADS<span class="chev chev--end"></span></h2>
    <div class="box box--red" style="left:29px;top:291px;width:373px;height:222px">
      <div class="salad-row">
        <div><div class="item-head"><span class="name">Garden Salad</span></div>
        <p class="item-desc">Lettuce, Tomatoes, Cucumbers, Olives, Onions, &amp; Pepperoncini.</p></div>
        <div class="sizes"><span>S<b>$4.99</b></span><span>M<b>$5.99</b></span><span>L<b>$8.99</b></span></div>
      </div>
      <div class="salad-row">
        <div><div class="item-head"><span class="name">Antipasto</span></div>
        <p class="item-desc">Ham, Salami, Lettuce, Tomatoes, Cucumbers, Olives, Onions, &amp; Pepperoncini. Topped with Mozzarella Cheese.</p></div>
        <div class="sizes"><span>S<b>$6.99</b></span><span>M<b>$8.99</b></span><span>L<b>$11.99</b></span></div>
      </div>
      <div class="salad-row">
        <div><div class="item-head"><span class="name">Bruiser Chicken Salad</span></div>
        <p class="item-desc">Chicken, Parmesan Cheese, Lettuce, Tomatoes, Cucumbers, Olives, Onions, &amp; Pepperoncini.</p></div>
        <div class="sizes"><span>S<b>$6.99</b></span><span>M<b>$8.99</b></span><span>L<b>$11.99</b></span></div>
      </div>
      <div class="salad-row">
        <div><div class="item-head"><span class="name">Caesar Salad</span></div>
        <p class="item-desc">Romaine Lettuce, Parmesan Cheese, Croutons - Tossed in Caesar Dressing.</p></div>
        <div class="sizes"><span>S<b>$5.49</b></span><span>M<b>$6.99</b></span><span>L<b>$9.99</b></span></div>
      </div>
      <div class="salad-row">
        <div><div class="item-head"><span class="name">Chicken Caesar Salad</span></div>
        <p class="item-desc">Chicken, Romaine Lettuce, Parmesan Cheese, Croutons - Tossed in Caesar Dressing.</p></div>
        <div class="sizes"><span>S<b>$6.99</b></span><span>M<b>$8.99</b></span><span>L<b>$11.99</b></span></div>
      </div>
    </div>

    <div class="dressings">
      <p class="label-red">Dressings:</p>
      <p>Ranch, Italian, Caesar, Blue Cheese, Balsamic, &amp; Vinaigrette.</p>
    </div>
  </section>

</main>
</body>
</html>
```